Marine Services Letterhead design

We need a letterhead design for an Australian owned company in Victoria named Q+Q Harbour Works Pty Ltd. We provide linesmen and launches to assist the large ships that come into port.
Our colour is orange.
The final design should have a strong nautical theme and communicate safety and reliability.
I would like to use the letter head on invoices so it should print to pdf well.

Target Market(s)

Owners and representatives of shipping companies. It is not for general public

Industry/Entity Type

Nautical

Requirements
Must have
• A shipping theme, not overly complicated, featuring safety orange colours but not all orange of course.
The letterhead should just sit at the top of the page so I can use for invoices.
Nice to have
• Something elegant and stylish
Should not have
• cartoons or pop art

```html
<!DOCTYPE html>
<html lang="en">
<head>
<meta charset="utf-8">
<title>Q+Q Harbour Works Pty Ltd – Letterhead</title>
<link href="https://fonts.googleapis.com/css2?family=Open+Sans:wght@400;600&display=swap" rel="stylesheet">
<style>
  :root {
    --backdrop: #efefef;
    --paper: #f8f8f8;
    --ink: #8a8a8a;
    --ink-dark: #6d6d6d;
    --safety-orange: #dca25f;
    --sea-green: #95bfa7;
    --sea-green-text: #7bb497;
    --watermark: #e6e6e6;
  }
  * { box-sizing: border-box; margin: 0; padding: 0; }
  html, body {
    width: 1200px; height: 1000px; overflow: hidden;
    background: var(--backdrop);
    font-family: "Open Sans", Arial, sans-serif;
  }
  .letterhead {
    position: absolute; left: 282px; top: 50px;
    width: 636px; height: 900px;
    background: var(--paper);
    box-shadow: 0 2px 10px rgba(0,0,0,0.08);
  }
  .brand {
    position: absolute; left: 0; right: 0; top: 52px;
    display: flex; justify-content: center; align-items: center; gap: 10px;
  }
  .brand-square { width: 16px; height: 16px; background: var(--safety-orange); }
  .brand-name { font-size: 17px; font-weight: 600; color: var(--safety-orange); letter-spacing: 0.3px; }
  .watermark-name {
    position: absolute; left: 0; right: 0; top: 520px;
    text-align: center; font-size: 38px; font-weight: 600;
    color: var(--watermark); letter-spacing: 1px;
  }
  .letter-body {
    position: absolute; left: 72px; top: 170px; width: 492px;
    font-size: 10px; line-height: 15px; color: var(--ink);
  }
  .letter-body p { margin-bottom: 15px; text-align: justify; }
  .letter-body .greeting, .letter-body .closing { text-align: left; }
  .signature {
    position: absolute; left: 360px; top: 600px; width: 150px; height: 44px;
    background: linear-gradient(90deg, rgba(60,60,60,0.10), rgba(60,60,60,0.18), rgba(60,60,60,0.10));
    border-radius: 22px;
  }
  .band-orange {
    position: absolute; left: 0; top: 790px; width: 372px; height: 10px;
    background: var(--safety-orange);
  }
  .contact {
    position: absolute; left: 392px; top: 800px;
    font-size: 8.5px; line-height: 12px; color: var(--ink-dark);
  }
  .contact .company { font-size: 11px; color: var(--sea-green-text); margin-bottom: 2px; }
  .contact-line { display: flex; align-items: center; gap: 4px; }
  .contact-line svg { width: 8px; height: 8px; fill: var(--sea-green-text); }
  .band-green {
    position: absolute; left: 382px; right: 0; top: 858px; height: 10px;
    background: var(--sea-green);
  }
</style>
</head>
<body>
  <main class="letterhead">
    <header class="brand">
      <span class="brand-square"></span>
      <span class="brand-name">Q+Q Harbour Works</span>
    </header>

    <div class="watermark-name" aria-hidden="true">Q+Q Harbour Works</div>

    <section class="letter-body">
      <p class="greeting">Dear Client,</p>
      <p>Lorem ipsum dolor sit amet, consectetur adipiscing elit. Nulla sodales nisi vitae lorem ipsum dolor sit amet, consectetur adipiscing elit. Suspendisse feugiat eros nisl, a facilisis risus eleifend sed. Aliquam mauris enim, fermentum eu lacinia sit amet, laoreet eu leo. Nullam eleifend nulla in libero tristique, ac vulputate odio tincidunt. Etiam non condimentum tortor. Integer suscipit neque nec odio porttitor cursus. Phasellus a sapien blandit, suscipit justo id, condimentum ante. Morbi tristique justo risus, id mattis dui molestie ut. Nullam volutpat ut quam commodo faucibus.</p>
      <p>Nulla tincidunt molestie libero vel pretium. Donec condimentum nulla sit amet risus semper imperdiet. Duis congue eros nec diam blandit, et pellentesque sapien auctor. Curabitur iaculis enim lectus, in imperdiet mauris mattis eget. Etiam ac ornare metus. Mauris risus leo, egestas at dolor a, ultrices viverra et. Mauris venenatis lobortis eros.</p>
      <p>Nullam auctor venenatis metus, eu pulvinar sapien dapibus non. Cum sociis natoque penatibus et magnis dis parturient montes, nascetur ridiculus mus. Praesent sed lorem eget tortor volutpat dictum vel vel ipsum. Morbi pulvinar non nisi in ultrices.</p>
      <p class="closing">Best regards,</p>
    </section>

    <div class="signature" role="img" aria-label="Handwritten signature of the sender"></div>

    <div class="band-orange"></div>

    <footer class="contact">
      <div class="company">Q+Q Harbour Works Pty Ltd</div>
      <div class="contact-line">
        <svg viewBox="0 0 10 10" aria-hidden="true"><path d="M5 0a3.5 3.5 0 0 0-3.5 3.5C1.5 6 5 10 5 10s3.5-4 3.5-6.5A3.5 3.5 0 0 0 5 0zm0 5a1.5 1.5 0 1 1 0-3 1.5 1.5 0 0 1 0 3z"/></svg>
        <span>PO Box 412 Seacliff 3990</span>
      </div>
      <div class="contact-line">
        <svg viewBox="0 0 10 10" aria-hidden="true"><path d="M2 0.5l2 2-1 1.2a6 6 0 0 0 3.3 3.3l1.2-1 2 2L8.3 9.5C4 9.5 0.5 6 0.5 1.7z"/></svg>
        <span>1300 000 418</span>
      </div>
      <div class="contact-line">
        <svg viewBox="0 0 10 10" aria-hidden="true"><rect x="2.5" y="0.5" width="5" height="9" rx="1"/></svg>
        <span>0400 123 987</span>
      </div>
    </footer>

    <div class="band-green"></div>
  </main>
</body>
</html>
```